Fashion Wholesale Product Page

We need a product page layout for a wholesale catalogue.
It will include a title, 3 images, short description, prices and size and colour options in an a5 page for print.
We'd like a design file that we can use to update with new products in the future.
All images and content will be provided.
The range we are selling is all about simplicity and minimalism so we'd love this to be reflected in the layout.

Target Market(s)

Young, fashion conscious women with a strong appreciation for good, simple design.

Industry/Entity Type

Fashion

Requirements
Must have
• Title - 'Triangle Bra'
Short Description - 'Perfect for a smaller bust, the triangle bra is divine simplicity. Featuring our well known triangle cut and darted cups, we have perfected this design for an optimal fit.'
Prices - Wholesale: $30 RRP: $60
Available in -
Colours Black, White, Grey Marle
Sizes XS, S, M, L

3 product images
Nice to have
• If it fits with the design it would be great to include the image on the model attached here.

I don't want it to feel too crowded though.

```html
<!DOCTYPE html>
<html lang="en">
<head>
<meta charset="utf-8">
<title>ELVA – Underwear + Basics Catalogue</title>
<link href="https://fonts.googleapis.com/css2?family=Raleway:wght@300;400;500&family=Varela+Round&display=swap" rel="stylesheet">
<style>
  :root {
    --backdrop: #e7e4e0;
    --paper: #ffffff;
    --ink: #3a3a3a;
    --ink-soft: #555555;
    --accent-red: #c8202f;
    --rule-grey: #a9a9a9;
    --page-edge: #d6d3cf;
    --photo-wall: #d9d6d1;
    --photo-skin: #c9a892;
  }
  * { box-sizing: border-box; margin: 0; padding: 0; }
  html, body { width: 1200px; height: 644px; overflow: hidden; }
  body {
    background: var(--backdrop);
    position: relative;
    font-family: "Varela Round", sans-serif;
    color: var(--ink);
  }
  .abs { position: absolute; }

  /* Cover */
  .cover {
    left: 70px; top: 75px; width: 330px; height: 473px;
    background: var(--paper);
    overflow: hidden;
    box-shadow: 0 0 0 1px var(--page-edge);
  }
  .cover-photo {
    position: absolute; inset: 0;
    background: linear-gradient(100deg, var(--photo-wall) 0%, #efeeec 45%, #e2e0dc 100%);
  }
  .cover-photo::after {
    content: ""; position: absolute; left: 20px; top: 60px; width: 190px; height: 413px;
    background: linear-gradient(180deg, var(--photo-skin) 0%, #2a2a2a 40%, var(--photo-skin) 55%, #d9cfcb 80%, #c7b3a6 100%);
    opacity: .55; border-radius: 90px 90px 0 0;
  }
  .cover-brand {
    position: absolute; left: 158px; top: 70px;
    font-family: "Raleway", sans-serif; font-weight: 300;
    font-size: 54px; letter-spacing: 1px; color: #111;
  }
  .cover-tagline {
    position: absolute; left: 184px; top: 372px;
    font-family: "Raleway", sans-serif; font-weight: 400;
    font-size: 17px; line-height: 24px; letter-spacing: .5px; color: #222;
  }

  /* Spread */
  .page {
    top: 72px; height: 476px; background: var(--paper);
    box-shadow: 0 0 0 1px var(--page-edge);
  }
  .page-left { left: 493px; width: 337px; }
  .page-right { left: 830px; width: 320px; }

  .model-photo {
    background: linear-gradient(180deg, #d8d4d0 0%, #cbb29f 18%, #2e2e2e 32%, #2e2e2e 62%, #c6a88f 78%, #d8d4d0 100%);
  }
  .accent-bar { height: 4px; background: var(--accent-red); }
  .rule { height: 2px; background: var(--rule-grey); }

  .product-title {
    font-family: "Raleway", sans-serif; font-weight: 500;
    font-size: 19px; letter-spacing: .5px; color: #222;
    padding-bottom: 2px; border-bottom: 3px solid var(--accent-red);
    white-space: nowrap; z-index: 2;
  }
  .product-copy { font-size: 9.5px; line-height: 12.5px; color: var(--ink-soft); }
  .product-copy p + p { margin-top: 10px; }
  .spec { font-size: 9.5px; line-height: 13px; color: var(--ink-soft); white-space: nowrap; }
  .spec-label { display: inline-block; width: 38px; color: var(--ink); }

  .product-shot { border-radius: 2px; }
  .shot-white { background: linear-gradient(180deg, #ffffff, #eeeeee); box-shadow: inset 0 0 0 1px #ececec; }
  .shot-grey { background: linear-gradient(180deg, #bdbdbd, #9e9e9e); }
  .shot-black { background: linear-gradient(180deg, #2b2b2b, #151515); }

  .folio { font-size: 9px; color: var(--ink); }
  .folio-brand { font-family: "Raleway", sans-serif; font-weight: 500; font-size: 10px; letter-spacing: 1px; color: #111; }
</style>
</head>
<body>

<!-- Cover -->
<section class="cover abs">
  <div class="cover-photo" role="img" aria-label="Model in a black bra and pale briefs against a white brick wall with a trailing vine"></div>
  <div class="cover-brand">ELVA</div>
  <div class="cover-tagline">UNDERWEAR<br>+ BASICS</div>
</section>

<!-- Left page: Bodysuit -->
<section class="page page-left abs"></section>
<div class="abs model-photo" style="left:500px;top:82px;width:141px;height:245px;" role="img" aria-label="Model wearing the black bodysuit"></div>
<div class="abs accent-bar" style="left:500px;top:326px;width:141px;"></div>

<h2 class="abs product-title" style="left:653px;top:92px;">BODYSUIT</h2>
<div class="abs product-copy" style="left:652px;top:140px;width:156px;">
  <p>Our famous bodysuit is back with a brand new design!</p>
  <p>First of all, we’ve lined the front for some extra support. Then we incorporated snap fasteners in the base for that extra ease in removal. Lastly, we’ve made the straps adjustable and they can now be configured to sit straight or criss cross.</p>
  <p>Is there anything this bodysuit can’t do?</p>
</div>
<div class="abs rule" style="left:643px;top:326px;width:158px;"></div>

<div class="abs spec" style="left:518px;top:337px;">Prices</div>
<div class="abs spec" style="left:518px;top:353px;">Wholesale: $X0&nbsp; RRP: $X0</div>
<div class="abs spec" style="left:652px;top:337px;">Colours Black, White, Grey Marle</div>
<div class="abs spec" style="left:652px;top:353px;"><span class="spec-label">Sizes</span> XS, S, M, L</div>
<div class="abs rule" style="left:505px;top:371px;width:296px;"></div>

<div class="abs product-shot shot-white" style="left:520px;top:380px;width:78px;height:150px;" role="img" aria-label="White bodysuit, flat product shot"></div>
<div class="abs product-shot shot-grey" style="left:628px;top:380px;width:78px;height:150px;" role="img" aria-label="Grey marle bodysuit, flat product shot"></div>
<div class="abs product-shot shot-black" style="left:728px;top:380px;width:78px;height:150px;" role="img" aria-label="Black bodysuit, flat product shot"></div>

<div class="abs folio" style="left:518px;top:535px;">2</div>
<div class="abs folio-brand" style="left:780px;top:535px;">ELVA</div>

<!-- Right page: Triangle Bra -->
<section class="page page-right abs"></section>
<div class="abs model-photo" style="left:1002px;top:82px;width:143px;height:244px;" role="img" aria-label="Model wearing the black triangle bra and high-waist briefs"></div>
<div class="abs accent-bar" style="left:1002px;top:325px;width:143px;"></div>

<h2 class="abs product-title" style="left:845px;top:85px;">TRIANGLE BRA</h2>
<div class="abs product-copy" style="left:845px;top:136px;width:152px;">
  <p>Perfect for a smaller bust, the triangle bra is divine simplicity.</p>
  <p>Featuring our well known triangle cut and darted cups, we have perfected this design for an optimal fit.</p>
</div>
<div class="abs spec" style="left:845px;top:244px;font-size:9px;">Prices Wholesale: $30 RRP: $60</div>
<div class="abs rule" style="left:843px;top:263px;width:150px;"></div>

<div class="abs spec" style="left:1003px;top:336px;"><span class="spec-label">Colours</span> Black, White,<br><span class="spec-label"></span> Grey Marle</div>
<div class="abs spec" style="left:1003px;top:366px;"><span class="spec-label">Sizes</span> XS, S, M, L</div>
<div class="abs rule" style="left:1003px;top:383px;width:143px;"></div>

<div class="abs product-shot shot-white" style="left:850px;top:282px;width:130px;height:106px;" role="img" aria-label="White triangle bra, flat product shot"></div>
<div class="abs product-shot shot-black" style="left:848px;top:410px;width:135px;height:110px;" role="img" aria-label="Black triangle bra, flat product shot"></div>
<div class="abs product-shot shot-grey" style="left:996px;top:410px;width:138px;height:110px;" role="img" aria-label="Grey marle triangle bra, flat product shot"></div>

<div class="abs folio-brand" style="left:843px;top:535px;">ELVA</div>
<div class="abs folio" style="left:1130px;top:535px;">3</div>

</body>
</html>
```